Vexo-Shine Janitorial Services

Looking for a modern design for my new business. I like the clear see through of the card I've attached. The business is built around The Prindle Omni 720 system, with that said I'd like to add the prindle logo on the bachside with the statement of Powered by (then the Prindle Logo). I really like the layout and color schemes of the card I attached. Black, Blue, and White. I would like to incorporate three images into the diamond shape, as seem in the layout.

Morton Quill
Managing Partner

```html
<!DOCTYPE html>
<html lang="en">
<head>
<meta charset="utf-8">
<title>Vexo-Shine Janitorial Services – Business Card</title>
<link rel="stylesheet" href="https://fonts.googleapis.com/css2?family=Marcellus&family=Montserrat:wght@400;500&display=swap">
<style>
  :root {
    --stage: #1c1c1e;
    --royal: #2264b0;
    --sky: #1eb3ea;
    --night: #1f2228;
    --night-soft: #3a3f48;
    --ink: #3b3f45;
    --white: #ffffff;
    --frame: #4fc3f0;
  }
  html, body { margin: 0; padding: 0; overflow: hidden; }
  body {
    width: 1200px; height: 900px;
    background: var(--stage);
    display: flex; flex-direction: column; align-items: center; justify-content: center;
    gap: 34px;
    font-family: "Montserrat", sans-serif;
  }
  .card {
    position: relative;
    width: 700px; height: 400px;
    overflow: hidden;
    box-shadow: 0 12px 30px rgba(0,0,0,0.55);
  }
  .card svg.card-art { position: absolute; inset: 0; }
  .brand { position: absolute; text-align: center; }
  .brand-mark {
    width: 70px; height: 70px; border-radius: 50%;
    background: var(--sky);
    margin: 0 auto 14px;
  }
  .brand-name {
    font-family: "Marcellus", serif;
    font-size: 40px; letter-spacing: 3px; line-height: 1;
  }
  .brand-tagline {
    font-family: "Marcellus", serif;
    font-size: 15px; letter-spacing: 2px; color: var(--royal);
    margin-top: 4px;
  }
  /* front */
  .card-front { background: var(--royal); }
  .card-front .brand { left: 330px; top: 150px; width: 260px; }
  .card-front .brand-name { color: var(--white); }
  .card-front .brand-tagline { color: #4f8fe0; }
  .powered {
    position: absolute; left: 48px; top: 260px;
    color: var(--white);
  }
  .powered-label { font-size: 11px; letter-spacing: 1px; margin-bottom: 10px; }
  .powered-partner { display: flex; align-items: center; gap: 12px; }
  .partner-name { font-size: 22px; font-weight: 500; color: var(--white); }
  .partner-dot { width: 40px; height: 40px; border-radius: 50%; background: var(--white); }
  /* back */
  .card-back { background: var(--white); }
  .card-back .brand { left: 450px; top: 110px; width: 250px; }
  .card-back .brand-name { color: var(--ink); }
  .contact {
    position: absolute; right: 270px; top: 292px;
    text-align: right; color: var(--ink); font-size: 16px; line-height: 1.6;
  }
  .contact-line { display: flex; align-items: center; justify-content: flex-end; gap: 10px; }
  .contact-line svg { width: 16px; height: 16px; }
  .divider {
    position: absolute; left: 448px; top: 292px;
    width: 2px; height: 54px; background: var(--royal);
  }
  .person { position: absolute; left: 470px; top: 286px; }
  .person-name { font-family: "Marcellus", serif; font-size: 30px; color: var(--ink); letter-spacing: 1px; }
  .person-role { font-size: 17px; color: var(--royal); }
</style>
</head>
<body>

<section class="card card-front">
  <svg class="card-art" viewBox="0 0 700 400" width="700" height="400">
    <defs>
      <linearGradient id="office-tone" x1="0" y1="0" x2="1" y2="1">
        <stop offset="0" stop-color="#2d3139"/>
        <stop offset="1" stop-color="#16181c"/>
      </linearGradient>
    </defs>
    <path class="office-scene" role="img" aria-label="Photo of a cleaner disinfecting an office"
          fill="url(#office-tone)"
          d="M0 0 L110 0 C430 20 660 170 660 270 C660 345 580 400 470 400 L0 400 Z"/>
    <path class="swoosh" fill="var(--sky)"
          d="M120 0 C420 20 650 150 665 270 C640 170 430 45 120 0 Z"/>
    <g class="service-diamonds" stroke="var(--frame)" stroke-width="2.5">
      <polygon role="img" aria-label="Photo of a yellow janitorial cart" fill="#7d8a74" points="160,35 215,90 160,145 105,90"/>
      <polygon role="img" aria-label="Photo of a disinfecting sprayer unit" fill="#8fa3ba" points="290,50 345,105 290,160 235,105"/>
      <polygon role="img" aria-label="Photo of a worker spraying disinfectant" fill="#6f7f92" points="225,105 285,165 225,225 165,165"/>
    </g>
  </svg>
  <div class="powered">
    <div class="powered-label">POWERED BY</div>
    <div class="powered-partner">
      <span class="partner-name">Prindle Omni 720</span>
      <span class="partner-dot"></span>
    </div>
  </div>
  <div class="brand">
    <div class="brand-mark"></div>
    <div class="brand-name">Vexo-Shine</div>
    <div class="brand-tagline">Janitorial Services</div>
  </div>
</section>

<section class="card card-back">
  <svg class="card-art" viewBox="0 0 700 400" width="700" height="400">
    <rect class="blue-field" width="700" height="400" fill="var(--royal)"/>
    <path class="white-field" fill="var(--white)"
          d="M120 400 C40 310 50 150 380 105 C520 88 640 92 700 96 L700 400 Z"/>
    <path class="swoosh" fill="var(--sky)"
          d="M95 200 C190 120 420 80 700 92 L700 104 C430 96 230 120 95 200 Z"/>
  </svg>
  <div class="brand">
    <div class="brand-mark"></div>
    <div class="brand-name">Vexo-Shine</div>
    <div class="brand-tagline">Janitorial Services</div>
  </div>
  <div class="contact">
    <div class="contact-line">000 000 0000
      <svg viewBox="0 0 16 16" fill="none" stroke="var(--royal)" stroke-width="1.4"><circle cx="8" cy="8" r="6.5"/><path d="M5.5 5c0 3 2.5 5.5 5.5 5.5l.5-1.5-1.5-.8-.8.8C8 8.5 7.5 8 7 7l.8-.8L7 4.7Z"/></svg>
    </div>
    <div class="contact-line">quill@vexoshine.com
      <svg viewBox="0 0 16 16" fill="none" stroke="var(--royal)" stroke-width="1.4"><rect x="1.5" y="3.5" width="13" height="9"/><path d="M1.5 3.5 8 9l6.5-5.5"/></svg>
    </div>
  </div>
  <div class="divider"></div>
  <div class="person">
    <div class="person-name">Morton Quill</div>
    <div class="person-role">Managing Partner</div>
  </div>
</section>

</body>
</html>
```